New Attorney in Non-Traditional Field Needs Creative Edgy Legal Business Card with Side Business Not

I need a new personal business card. Away from the silver lettering on heavy white card stock, Velvet Harbor anyone? I'm newly admitted to the CA bar, I started my own small side-business in sales, I'm arbitrating on a part time basis, and I'm creating a ClipTower channel about current news from young professionals' perspective in January. On the side I've been taking a lot of home buying negotiation classes, and I do a lot of yoga. It would be my dream job to advise clients in the startup/entrepreneurial world. I would like my Cliptower channel, website (www.marenquill.example/dankorbel), phone number, email, admittance #, and link for worklinx featured on my card. The colors and message of homepage www.bluefernmat.example really speak to me. Often I'll read that Hedda Pallin quote about doing one thing for your brand everyday, and I believe it in wholeheartedly.
Updates

Merrin's design has been accepted with very minimal changes. Thank you all for your submissions. This has been a fun experience.

Target Market(s)

all young attorneys, small startups, small tech, potential employers, networking events for lawyers and other young professionals

Industry/Entity Type

Business

Contact Information for Business Card

Dorothea K. Banfield, Esq.
Attorney bar card number
Ph (555) 407-1186
Email Dot.Banfield@postkite.example
Work linx website
Cliptower Channel coming soon!
Maren & Quill website

Font styles to use
Sans Serif
Decorative

Requirements
Must have
• A simple image or logo that can transition to other products as I build my brand. Great colors. Maybe all white & gold? Maybe a cool blues/purples motif?

```html
<!DOCTYPE html>
<html lang="en">
<head>
<meta charset="utf-8">
<title>Dorothea K. Banfield, Esq. — Business Card</title>
<link rel="stylesheet" href="https://fonts.googleapis.com/css2?family=Cormorant+Garamond:wght@500&family=Cutive+Mono&display=swap">
<style>
  :root {
    --backdrop: #8d8d90;
    --card-wine: #4b1a27;
    --ink-white: #ffffff;
    --gold: #e6b43c;
    --gold-soft: #c99a34;
  }
  * { box-sizing: border-box; margin: 0; padding: 0; }
  html, body {
    width: 1200px;
    height: 638px;
    overflow: hidden;
    background: var(--backdrop);
  }
  .stage {
    width: 1200px;
    height: 638px;
    display: flex;
    align-items: center;
    justify-content: center;
    gap: 40px;
  }
  .card {
    position: relative;
    width: 520px;
    height: 297px;
    background: var(--card-wine);
    color: var(--ink-white);
    font-family: "Cormorant Garamond", Georgia, serif;
    font-weight: 500;
    box-shadow: 0 6px 18px rgba(0, 0, 0, 0.25);
  }

  /* Brand mark: name in card type with one plain circle beside it */
  .brand {
    position: absolute;
    left: 0;
    right: 0;
    display: flex;
    align-items: center;
    justify-content: center;
    color: var(--ink-white);
    letter-spacing: 0.02em;
  }
  .brand-dot {
    border: 1.5px solid var(--ink-white);
    border-radius: 50%;
    flex: none;
  }
  .card-back .brand {
    top: 110px;
    height: 80px;
    gap: 18px;
    font-size: 64px;
  }
  .card-back .brand-dot { width: 44px; height: 44px; }
  .card-front .brand {
    top: 44px;
    height: 40px;
    gap: 8px;
    font-size: 24px;
  }
  .card-front .brand-dot { width: 16px; height: 16px; border-width: 1px; }

  /* Front details */
  .name {
    position: absolute;
    left: 0;
    right: 0;
    top: 100px;
    text-align: center;
    font-size: 28px;
    font-weight: 500;
    letter-spacing: 0.03em;
    white-space: nowrap;
  }
  .phone {
    position: absolute;
    left: 0;
    right: 0;
    top: 158px;
    text-align: center;
    font-family: "Cutive Mono", "Courier New", monospace;
    font-size: 16px;
    letter-spacing: 0.08em;
  }
  .rule {
    position: absolute;
    left: 24px;
    top: 140px;
    width: 472px;
    height: 60px;
  }
  .ornament {
    position: absolute;
    left: 222px;
    top: 186px;
    width: 76px;
    height: 12px;
    border-radius: 50%;
    background: radial-gradient(ellipse at center, var(--gold) 0%, var(--gold-soft) 55%, rgba(201, 154, 52, 0) 100%);
  }
</style>
</head>
<body>
  <main class="stage">
    <section class="card card-back" aria-label="Card back">
      <div class="brand"><span class="brand-dot"></span><span class="brand-name">Banfield</span></div>
    </section>

    <section class="card card-front" aria-label="Card front">
      <div class="brand"><span class="brand-dot"></span><span class="brand-name">Banfield</span></div>
      <h1 class="name">DOROTHEA K. BANFIELD, Esq.</h1>
      <svg class="rule" viewBox="0 0 472 60" aria-hidden="true">
        <defs>
          <linearGradient id="gold-fade" x1="0" x2="1" y1="0" y2="0">
            <stop offset="0" style="stop-color: var(--gold-soft); stop-opacity: 0.15"/>
            <stop offset="0.5" style="stop-color: var(--gold); stop-opacity: 1"/>
            <stop offset="1" style="stop-color: var(--gold-soft); stop-opacity: 0.15"/>
          </linearGradient>
        </defs>
        <line x1="0" y1="10" x2="472" y2="10" stroke="url(#gold-fade)" stroke-width="1.2"/>
        <line x1="20" y1="52" x2="190" y2="52" stroke="url(#gold-fade)" stroke-width="1.5"/>
        <line x1="282" y1="52" x2="452" y2="52" stroke="url(#gold-fade)" stroke-width="1.5"/>
      </svg>
      <p class="phone">Ph (555) 407-1186</p>
      <div class="ornament" role="img" aria-label="Small gold scroll ornament at the centre of the divider"></div>
    </section>
  </main>
</body>
</html>
```